Soap box for artisan soaps, eco-look, high design

We need a soap box for our lovely artisan soaps. The box size is: 9 cm height x 6,5 cm width x 2,8 cm depth. It would be nice when there is a small window in the box so you can see the soap.

See attachment for an example soap box (upside down). Please use the same elements such as texts and industrie logos. The idea is that we have a generic design that we can custom-made for different soaps. We have 15 different soaps in total at the moment.

Target Market(s)

Middle to high income

Font styles to use
Decorative
Script

Requirements
Must have
• Dutch text:
• Etherische oliën
• Handgemaakt
• Natuurlijke ingrediënten

```html
<!DOCTYPE html>
<html lang="nl">
<head>
<meta charset="utf-8">
<title>Velora – zeepdoos Lavender</title>
<link href="https://fonts.googleapis.com/css2?family=Playfair+Display:wght@700;900&family=Jost:wght@300;400;600&display=swap" rel="stylesheet">
<style>
  :root {
    --kraft: #b58d62;
    --kraft-dark: #a9825a;
    --ink: #231a13;
    --cut: #ffffff;
    --fold: #e3221b;
    --cream: #f6f0c4;
    --lavender-deep: #4a4f8e;
    --lavender-mid: #7d6fb0;
    --foam: #eeecd6;
  }
  html, body { margin: 0; padding: 0; width: 1200px; height: 1162px; overflow: hidden; background: var(--kraft); }
  .sheet {
    position: relative; width: 1500px; height: 1452px;
    transform: scale(0.8); transform-origin: 0 0;
    background: radial-gradient(ellipse at 40% 30%, #ba9267 0%, var(--kraft) 55%, var(--kraft-dark) 100%);
    font-family: "Jost", sans-serif; color: var(--ink);
  }
  .dieline { position: absolute; inset: 0; width: 1500px; height: 1452px; }
  .dieline .cut { fill: none; stroke: var(--cut); stroke-width: 2; }
  .dieline .fold { fill: none; stroke: var(--fold); stroke-width: 2; }

  .panel { position: absolute; }
  .panel--back { left: 383px; top: 85px; width: 732px; height: 477px; transform: rotate(180deg); }
  .panel--ingredients { left: 386px; top: 562px; width: 727px; height: 204px; transform: rotate(180deg); }
  .panel--front { left: 386px; top: 766px; width: 727px; height: 477px; }
  .panel--bottom { left: 386px; top: 1243px; width: 727px; height: 202px; }

  .story-title { position: absolute; left: 40px; top: 30px; margin: 0; font: 900 30px/1 "Playfair Display", serif; }
  .story-text { position: absolute; left: 37px; top: 86px; width: 378px; margin: 0; font: 400 15.5px/24.6px "Jost", sans-serif; text-align: justify; letter-spacing: 0.3px; }
  .free-box { position: absolute; left: 468px; top: 36px; width: 222px; height: 162px; border: 1.5px solid var(--cut); box-sizing: border-box; padding: 16px 20px; font: 300 14px/21px "Jost", sans-serif; }
  .free-box h3 { margin: 0 0 2px; font: 900 20px/1.2 "Playfair Display", serif; }
  .free-box p { margin: 0; }
  .brand-name { font-family: "Playfair Display", serif; font-weight: 900; color: var(--ink); }
  .back-brand { position: absolute; left: 503px; top: 228px; margin: 0; font-size: 48px; line-height: 1; }
  .origin { position: absolute; left: 505px; top: 306px; font: 300 12px/1 "Jost", sans-serif; }
  .web { position: absolute; left: 505px; top: 330px; font: 700 15px/1 "Playfair Display", serif; }
  .weight { position: absolute; left: 463px; top: 384px; font: 900 26px/1 "Playfair Display", serif; }
  .icon-recycle { position: absolute; left: 575px; top: 384px; width: 40px; height: 40px; border-radius: 50%; background: var(--ink); }
  .icon-pao { position: absolute; left: 631px; top: 386px; width: 36px; height: 36px; border: 3px solid var(--ink); border-radius: 10px; box-sizing: border-box; }
  .signature { position: absolute; left: 85px; top: 372px; width: 265px; height: 50px; border-radius: 25px; background: rgba(255,255,255,0.18); }

  .ingredients-text { position: absolute; left: 63px; top: 58px; width: 600px; margin: 0; font: 400 14px/20.5px "Jost", sans-serif; text-align: justify; }
  .ingredients-text strong { font-weight: 600; }

  .scent-lettering { position: absolute; left: 239px; top: 24px; width: 240px; height: 125px; border-radius: 40px 60px 30px 50px; background: linear-gradient(160deg, var(--cream), rgba(246,240,196,0.55)); }
  .bath-art { position: absolute; left: 184px; top: 164px; width: 355px; height: 220px; border-radius: 40px 40px 90px 90px; background: radial-gradient(ellipse at 50% 40%, var(--foam) 0%, #c9c4d8 40%, var(--lavender-mid) 70%, var(--lavender-deep) 100%); }
  .front-brand { position: absolute; left: 0; width: 727px; top: 412px; margin: 0; text-align: center; color: #fffdf5; font: 900 40px/1 "Playfair Display", serif; }

  .bottom-text { position: absolute; left: 64px; top: 40px; width: 376px; margin: 0; font: 400 15px/20.8px "Jost", sans-serif; text-align: justify; }
  .bottom-brand { position: absolute; left: 502px; top: 108px; margin: 0; font-size: 52px; line-height: 1; }
</style>
</head>
<body>
<div class="sheet">
  <svg class="dieline" viewBox="0 0 1500 1452" aria-hidden="true">
    <path class="cut" d="M385,85 L410,5 L1090,5 L1115,85"/>
    <path class="cut" d="M383,87 H150 M150,87 V128 H188 M150,87 Q80,90 25,160 V490 Q80,560 150,562 V520 H190 M150,562 H383"/>
    <path class="cut" d="M1117,87 H1350 M1350,87 V128 H1312 M1350,87 Q1420,90 1475,160 V490 Q1420,560 1350,562 V520 H1310 M1350,562 H1117"/>
    <path class="cut" d="M386,566 L173,592 V714 L386,764"/>
    <path class="cut" d="M1113,566 L1327,592 V714 L1113,764"/>
    <path class="cut" d="M386,766 V1243 M1113,766 V1243"/>
    <path class="cut" d="M386,1245 L173,1293 V1420 L386,1445"/>
    <path class="cut" d="M1113,1245 L1327,1293 V1420 L1113,1445"/>
    <path class="fold" d="M158,130 V520 M1342,130 V520"/>
    <rect class="fold" x="383" y="85" width="732" height="477"/>
    <rect class="fold" x="386" y="562" width="727" height="204"/>
    <rect class="fold" x="386" y="1243" width="727" height="202"/>
  </svg>

  <section class="panel panel--back">
    <h2 class="story-title">Onze zeep</h2>
    <p class="story-text">Het geeft jouw huid een heerlijk gevoel met zachte bubbels en rijke geur! Handgemaakt in kleine batches met eerlijke ingrediënten en essentiële oliën. Elke zeep wordt alleen geproduceerd als het iets goeds voor je doet en droogt minstens zes weken voordat ze worden verpakt. Ze zien er te mooi uit om te openen, maar hoe ga je dan genieten van de heerlijke bubbels, de ongelooflijke geur en je zachte, zijdeachtige huid?</p>
    <div class="free-box">
      <h3>Vrij van:</h3>
      <p>SLA &amp; SLSA<br>Alcohol &amp; Parabenen<br>Sorbaten &amp; Siliconen<br>Sulfaat &amp; Conserverings-<br>middelen</p>
    </div>
    <p class="brand-name back-brand">Velora</p>
    <span class="origin">Westhaven, Nederland</span>
    <span class="web">velora.nl</span>
    <span class="weight">120g ℮</span>
    <span class="icon-recycle" role="img" aria-label="Recyclingsymbool"></span>
    <span class="icon-pao" role="img" aria-label="Houdbaarheid na openen, 24 maanden"></span>
    <div class="signature" role="img" aria-label="Handgeschreven handtekening van de maker"></div>
  </section>

  <section class="panel panel--ingredients">
    <p class="ingredients-text"><strong>Ingredients:</strong> Olijf olie pomace (Olea europaea), Kokosnoot olie (Cocos nucifera), Palm olie (Elaeis Guineensis Kernel Oil), Water (Aqua), Citroen Etherische Olie (Citrus limonum), maanzaad (Papaver somniferum), Ijzer oxide geel (Iron Oxide). Natuurlijke bestanddelen van Etherische Olie – Citral, Citronellol, Geraniol, Limonene, Linalool.</p>
  </section>

  <section class="panel panel--front">
    <div class="scent-lettering" role="img" aria-label="Handgeletterde geurnaam Lavender"></div>
    <div class="bath-art" role="img" aria-label="Illustratie van een lavendelkleurig bad vol schuim"></div>
    <p class="front-brand">Velora</p>
  </section>

  <section class="panel panel--bottom">
    <p class="bottom-text">Essentiële oliën van Lemon creëren een levendige explosie van positieve goodness, waardoor u vrolijk wakker word. Poppy seeds worden toegevoegd om een beetje kracht te geven bij het exfoliëren. *Lemon helpt je in een positieve state of mind te komen, waardoor je de dag beter aan kan.</p>
    <p class="brand-name bottom-brand">Velora</p>
  </section>
</div>
</body>
</html>
```